Carrowind Year 9 Curriculum Model

We need a graphic that communicates all the overlapping elements of our new curriculum. Perhaps it could involve a series of concentric circles moving out from the centre:
1. the "Ideal Learner" profile at the centre with the school's logo behind it (see uploaded file).
2. The words of the "General Capabilities" from the Australian national curriculum in the next circle moving out of centre: "Ethical Understanding" "Literacy" "Numeracy" "Intercultural Awareness" "ICT Capacity" "Critical and Creative Thinking" "Personal and Social Capability"
3. Next circle out has the subjects: "Mathematics" "English" "Languages" "Health and Physical Education" "Technology" "Religious Education" "Humanities" "Arts" "Science"
4. Next Circle out has the title "Community" and then less important, the words "Local" "Regional" "National"
5. Next circle out is simple called "World"
6. Next circle out is simply called "Future"
IF there is a way to make it look not too bad...:Overlaying all the other aspects, floating somewhere, are the 3 significant priorities for the curriculum: Asia, Indigenous Culture and Sustainability

Target Market(s)

Year 9 (15 year old) school students and their parents, as well as teachers and other visitors to the school. It will be used to explain the curriculum and have on the walls as a reminder.

Industry/Entity Type

School

Requirements
Must have
• All of the words in the brief, with a relational dimension for each.

```html
<!DOCTYPE html>
<html lang="en">
<head>
<meta charset="utf-8">
<title>Carrowind Year 9 Curriculum Model</title>
<link rel="stylesheet" href="https://fonts.googleapis.com/css2?family=Oswald:wght@500;600&family=Alfa+Slab+One&display=swap">
<style>
  :root {
    --page: #ffffff;
    --ink-light: #ffffff;
    --ink-dark: #000000;
    --night: #000000;
    --glow-future: #18e030;
    --glow-world: #9a1a8e;
    --glow-community: #e41212;
    --glow-subjects: #c8306c;
    --glow-capabilities: #1414ff;
    --heading-gold: #ffff00;
    --core-yellow: #ffff00;
    --flat-future: #1e7b1e;
    --flat-world: #ffcc00;
    --flat-community: #cc0000;
    --flat-subjects: #6600cc;
    --flat-capabilities: #ff9900;
    --flat-core-text: #00ff00;
    --flat-label-gold: #ffcc00;
    --flat-label-brown: #4a2410;
    --ring: #ffffff;
  }
  * { margin: 0; padding: 0; box-sizing: border-box; }
  html, body { width: 1200px; height: 1000px; overflow: hidden; background: var(--page); }
  .canvas { position: relative; width: 1200px; height: 1000px; overflow: hidden; }

  .model { position: absolute; width: 640px; height: 540px; }
  .model--glow { left: 0; top: 0; }
  .model--flat { left: 517px; top: 415px; }

  .bubble { position: absolute; border-radius: 50%; }
  .bubble--future { left: 158px; top: 112px; width: 122px; height: 122px; }
  .bubble--world { left: 259px; top: 39px; width: 124px; height: 124px; }
  .bubble--community { left: 381px; top: 31px; width: 200px; height: 200px; }
  .bubble--subjects { left: 43px; top: 232px; width: 296px; height: 296px; }
  .bubble--capabilities { left: 338px; top: 232px; width: 296px; height: 296px; }
  .bubble--core { left: 245px; top: 147px; width: 186px; height: 186px; border: 5px solid var(--ring); }

  .model--glow .bubble--future { background: radial-gradient(circle, var(--glow-future) 0%, #08700e 22%, var(--night) 62%); }
  .model--glow .bubble--world { background: radial-gradient(circle, var(--glow-world) 0%, #3a0838 25%, var(--night) 62%); }
  .model--glow .bubble--community { background: radial-gradient(circle at 50% 48%, var(--glow-community) 0%, #6a0606 30%, var(--night) 68%); }
  .model--glow .bubble--subjects { background: radial-gradient(circle at 50% 42%, var(--glow-subjects) 0%, #5c0f30 28%, var(--night) 66%); }
  .model--glow .bubble--capabilities { background: radial-gradient(circle at 52% 46%, var(--glow-capabilities) 0%, #08086e 28%, var(--night) 66%); }
  .model--glow .bubble--core { background: var(--core-yellow); }

  .model--flat .bubble--future { background: var(--flat-future); }
  .model--flat .bubble--world { background: var(--flat-world); }
  .model--flat .bubble--community { background: var(--flat-community); }
  .model--flat .bubble--subjects { background: var(--flat-subjects); }
  .model--flat .bubble--capabilities { background: var(--flat-capabilities); }
  .model--flat .bubble--core { background: radial-gradient(circle, #1a1a1a 0%, var(--night) 70%); }

  .label {
    position: absolute;
    font-family: "Oswald", "Arial Narrow", sans-serif;
    font-weight: 600;
    font-size: 20px;
    line-height: 1;
    text-transform: uppercase;
    letter-spacing: -0.3px;
    white-space: nowrap;
  }
  .label--future { left: 218px; top: 162px; transform: translateX(-50%); }
  .label--world { left: 321px; top: 92px; transform: translateX(-50%); }
  .label--community { left: 426px; top: 99px; }
  .label--capabilities { left: 404px; top: 302px; }

  .model--glow .label--future,
  .model--glow .label--world { color: var(--ink-light); }
  .model--glow .label--community,
  .model--glow .label--capabilities { color: var(--heading-gold); }
  .model--flat .label--future { color: var(--flat-label-gold); }
  .model--flat .label--world { color: var(--flat-label-brown); }
  .model--flat .label--community { color: var(--flat-label-gold); }
  .model--flat .label--capabilities { color: var(--flat-label-brown); }

  .items {
    position: absolute;
    list-style: none;
    font-family: "Oswald", "Arial Narrow", sans-serif;
    font-weight: 500;
    font-size: 14px;
    line-height: 21.3px;
    color: var(--ink-light);
  }
  .items li { position: relative; padding-left: 14px; }
  .items li::before {
    content: "";
    position: absolute;
    left: 1px; top: 9px;
    width: 4px; height: 4px;
    border-radius: 50%;
    background: var(--ink-light);
  }
  .items--community { left: 427px; top: 120px; }
  .items--subjects { left: 109px; top: 297px; }
  .items--capabilities { left: 405px; top: 325px; width: 215px; }

  .core-title {
    position: absolute;
    left: 245px; top: 196px;
    width: 186px;
    text-align: center;
    font-family: "Alfa Slab One", "Rockwell", serif;
    font-size: 23px;
    line-height: 29px;
    letter-spacing: 1px;
    text-transform: uppercase;
  }
  .model--glow .core-title { color: var(--ink-dark); }
  .model--flat .core-title { color: var(--flat-core-text); }
</style>
</head>
<body>
<main class="canvas">

  <section class="model model--glow" aria-label="Carrowind curriculum model, glowing version">
    <div class="bubble bubble--future"></div>
    <div class="bubble bubble--world"></div>
    <div class="bubble bubble--community"></div>
    <div class="bubble bubble--subjects"></div>
    <div class="bubble bubble--capabilities"></div>
    <div class="bubble bubble--core"></div>

    <h2 class="label label--future">Future</h2>
    <h2 class="label label--world">World</h2>
    <h2 class="label label--community">Community</h2>
    <ul class="items items--community"><li>Local</li><li>Regional</li><li>National</li></ul>
    <ul class="items items--subjects">
      <li>Mathematics</li><li>English</li><li>Languages</li><li>Health and Physical Education</li>
      <li>Technology</li><li>Religious Education</li><li>Humanities</li><li>Arts</li><li>Science</li>
    </ul>
    <h2 class="label label--capabilities">General Capabilities</h2>
    <ul class="items items--capabilities">
      <li>Ethical Understanding</li><li>Literacy</li><li>Numeracy</li><li>Intercultural Awareness</li>
      <li>ICT Capacity</li><li>Critical and Creative</li><li>Thinking Personal and Social Capability</li>
    </ul>
    <h1 class="core-title">Ideal<br>Carrowind<br>Learner</h1>
  </section>

  <section class="model model--flat" aria-label="Carrowind curriculum model, flat colour version">
    <div class="bubble bubble--future"></div>
    <div class="bubble bubble--world"></div>
    <div class="bubble bubble--community"></div>
    <div class="bubble bubble--subjects"></div>
    <div class="bubble bubble--capabilities"></div>
    <div class="bubble bubble--core"></div>

    <h2 class="label label--future">Future</h2>
    <h2 class="label label--world">World</h2>
    <h2 class="label label--community">Community</h2>
    <ul class="items items--community"><li>Local</li><li>Regional</li><li>National</li></ul>
    <ul class="items items--subjects">
      <li>Mathematics</li><li>English</li><li>Languages</li><li>Health and Physical Education</li>
      <li>Technology</li><li>Religious Education</li><li>Humanities</li><li>Arts</li><li>Science</li>
    </ul>
    <h2 class="label label--capabilities">General Capabilities</h2>
    <ul class="items items--capabilities">
      <li>Ethical Understanding</li><li>Literacy</li><li>Numeracy</li><li>Intercultural Awareness</li>
      <li>ICT Capacity</li><li>Critical and Creative</li><li>Thinking Personal and Social Capability</li>
    </ul>
    <h1 class="core-title">Ideal<br>Carrowind<br>Learner</h1>
  </section>

</main>
</body>
</html>
```